Simple, bright, clean website - 3 pages, easy to update with WordPress!

I want to update my website (brelvatix.com) with a brighter/cleaner interface. It is quite dark right now. I would like it to be similar to a partner site (https://www.nodavent-44.com/). White with some orange highlights (matching the logo). I want to be able to easily update the site content. There should be 3 main pages: About, Services, Contact. I also like a design similar to quorfen.com

Target Market(s)

Anyone using technology to achieve business goals.

Industry/Entity Type

Managed Service Provider (IT)

Coding

Coded - Design and coding required

Number of Pages Required

3 page

Colors
F0912C
F2A743
F7CA91
FBE8D2
FDF5EE

Requirements
Must have
• Links to standard social media apps like WorkLattice, Pallgrove, etc.. Easy to edit and add pages.

```html
<!DOCTYPE html>
<html lang="en">
<head>
<meta charset="utf-8">
<title>Brelvatix Consulting Inc</title>
<link href="https://fonts.googleapis.com/css2?family=Exo+2:wght@300;400;500;600;700&display=swap" rel="stylesheet">
<style>
:root{
  --orange:#e39306;
  --orange-bright:#f0912c;
  --orange-soft:#f2a743;
  --cream:#fdf7ec;
  --dark:#262626;
  --ink:#1e1e1e;
  --grey:#4f4f4f;
  --body:#3c3c3c;
  --white:#ffffff;
}
*{margin:0;padding:0;box-sizing:border-box}
html,body{width:1200px;height:3222px;overflow:hidden}
body{font-family:"Exo 2",sans-serif;color:var(--ink);background:var(--white);position:relative}
.abs{position:absolute}
a{color:inherit;text-decoration:none}
.btn{position:absolute;display:flex;align-items:center;justify-content:center;background:var(--orange);color:var(--white);font-size:10px;font-weight:700;border-radius:16px}

.topbar{position:absolute;left:0;top:0;width:1200px;height:44px;background:var(--dark);color:var(--white);font-size:11px}
.topbar .phone{left:188px;top:14px;display:flex;align-items:center;gap:12px}
.topbar .mail{right:188px;top:14px;display:flex;align-items:center;gap:12px}

.header{position:absolute;left:0;top:44px;width:1200px;height:569px;background:var(--cream)}
.logo-text{position:absolute;font-weight:300;letter-spacing:1px}
.header .logo-text{left:188px;top:20px;font-size:30px;color:var(--grey)}
.nav{position:absolute;top:35px;font-size:11px;color:var(--ink)}
.hero-title{position:absolute;left:0;width:1200px;top:162px;text-align:center;font-size:49px;font-weight:700;line-height:52px;color:#474747}
.hero-text{position:absolute;left:262px;width:676px;top:335px;text-align:center;font-size:10.5px;line-height:17.5px;color:var(--body)}

.band{position:absolute;left:0;top:613px;width:1200px;height:190px;background:var(--orange);color:var(--white);text-align:center;font-size:32px;font-weight:500;line-height:45px;padding-top:50px}

.sky{position:absolute;left:0;top:803px;width:1200px;height:612px;background:linear-gradient(160deg,#9cc6ef 0%,#5d9ee0 45%,#2a6cb8 75%,#123f7a 100%)}
.sky h2{position:absolute;left:188px;top:62px;font-size:34px;font-weight:600;line-height:46px;color:var(--ink)}
.sky p{position:absolute;left:188px;top:166px;width:375px;font-size:9.5px;line-height:17.5px;color:var(--ink)}

.services{position:absolute;left:0;top:1415px;width:1200px;height:903px;background:var(--white)}
.section-title{position:absolute;left:0;width:1200px;top:68px;text-align:center;font-size:34px;font-weight:600;line-height:44px;color:#4a4a4a}
.svc{position:absolute;width:218px}
.svc h3{font-size:19px;font-weight:600;line-height:29px;color:var(--ink);margin-bottom:8px}
.svc p{font-size:9px;line-height:17.5px;color:var(--body)}
.card{position:absolute;left:463px;top:204px;width:274px;height:281px;background:var(--white);box-shadow:0 4px 18px rgba(0,0,0,.12)}
.card-icon{position:absolute;left:459px;top:204px;width:60px;height:60px;border-radius:50%;background:var(--orange);display:flex;align-items:center;justify-content:center}
.divider{position:absolute;left:463px;top:558px;width:1px;height:175px;background:#d8d8d8}
.view-all{left:528px;top:797px;width:143px;height:32px;border-radius:0}

.blog{position:absolute;left:0;top:2318px;width:1200px;height:633px;background:var(--cream)}
.blog h2{position:absolute;left:188px;top:68px;font-size:35px;font-weight:600;line-height:46px;color:var(--ink)}
.blog .intro{position:absolute;left:188px;top:172px;width:580px;font-size:9.5px;line-height:17.5px;color:var(--body)}
.post{position:absolute;top:243px;width:263px}
.post .thumb{width:263px;height:216px}
.post .date{margin-top:26px;font-size:12px;color:var(--orange)}
.post h3{margin-top:6px;font-size:19px;font-weight:600;line-height:31px;color:var(--ink);white-space:nowrap}

.footer{position:absolute;left:0;top:2951px;width:1200px;height:215px;background:var(--dark);color:var(--white)}
.footer .logo-text{left:257px;top:56px;font-size:42px;color:var(--white)}
.social{position:absolute;left:262px;top:124px;display:flex;gap:10px}
.social a{display:flex;align-items:center;gap:5px;font-size:10px}
.social a::before{content:"";width:10px;height:10px;border-radius:50%;border:1.5px solid var(--white)}
.social a.active::before{background:var(--orange-bright);border-color:var(--orange-bright)}
.foot-nav{position:absolute;left:619px;top:71px;display:flex;gap:24px;font-size:12px}
.foot-contact{position:absolute;right:256px;font-size:10.5px;display:flex;align-items:center;gap:12px}
.copyright{position:absolute;left:0;top:3166px;width:1200px;height:56px;text-align:center;font-size:11px;line-height:56px;color:var(--body)}
</style>
</head>
<body>

<div class="topbar">
  <div class="abs phone">
    <svg width="16" height="16" viewBox="0 0 24 24"><path d="M6.6 10.8a15.1 15.1 0 006.6 6.6l2.2-2.2c.3-.3.7-.4 1-.2 1.1.4 2.3.6 3.6.6.6 0 1 .4 1 1V20c0 .6-.4 1-1 1A17 17 0 013 4c0-.6.4-1 1-1h3.5c.6 0 1 .4 1 1 0 1.3.2 2.5.6 3.6.1.3 0 .7-.2 1z" fill="#f0912c"/></svg>
    <span>555-014-2290</span>
  </div>
  <div class="abs mail">
    <span>info@brelvatix.com</span>
    <svg width="15" height="12" viewBox="0 0 15 12"><rect width="15" height="12" rx="1" fill="#f0912c"/><path d="M1 1.5l6.5 5 6.5-5" stroke="#262626" stroke-width="1.4" fill="none"/></svg>
  </div>
</div>

<header class="header">
  <div class="logo-text">brelvatix</div>
  <a class="nav" style="left:724px">About</a>
  <a class="nav" style="left:792px">Services</a>
  <a class="nav" style="left:870px">Resources</a>
  <a class="nav" style="left:958px">Contact us</a>
  <h1 class="hero-title">Your Partner in<br>Transformative Business<br>Solutions</h1>
  <p class="hero-text">Brelvatix knows that a business builds its foundation with information and communication. You need the right technology to succeed in today's world. We establish long term partnerships with our clients to deliver operational efficiencies, reduce complexities and increase productivity.</p>
  <a class="btn" style="left:525px;top:413px;width:150px;height:29px">Learn More</a>
</header>

<section class="band">Brelvatix understands that technology is a tool to<br>improve your business productivity.</section>

<section class="sky" role="img" aria-label="Photo looking up at a glass office tower against a blue sky">
  <h2>Empowering Growth Through<br>Strategic Solutions</h2>
  <p>From day one, Brelvatix has strived to serve its clients with honesty and integrity while providing them with the best technology solutions for their business needs. In doing so, we evoke teamwork and client collaboration to earn the privilege to be</p>
  <a class="btn" style="left:188px;top:262px;width:149px;height:30px">Read More</a>
</section>

<section class="services">
  <h2 class="section-title">Empowering Growth Through<br>Strategic Solutions</h2>
  <div class="card"></div>
  <div class="card-icon">
    <svg width="30" height="30" viewBox="0 0 24 24" fill="none" stroke="#fff" stroke-width="2"><path d="M4 14v-2a8 8 0 0116 0v2"/><rect x="3" y="13" width="4" height="6" rx="1.5" fill="#fff"/><rect x="17" y="13" width="4" height="6" rx="1.5" fill="#fff"/></svg>
  </div>
  <div class="svc" style="left:218px;top:278px">
    <h3>Computer Installation<br>&amp; Deployment</h3>
    <p>Our experienced computer support team provides secure installation, deployment and configuration of servers and desktops in new or existing environments.</p>
  </div>
  <div class="svc" style="left:488px;top:269px;width:230px">
    <h3>Computer Maintenance<br>&amp; Support</h3>
    <p>Our computer consultants in Marrowdale offer fully outsourced management, regularly scheduled maintenance, as needed or on-call support, and emergency troubleshooting to meet your individual needs.</p>
  </div>
  <div class="svc" style="left:768px;top:260px">
    <h3>Server Configuration<br>&amp; Administration</h3>
    <p>Our consultants provide server configuration and support over a variety of OS and hardware platforms in the Intranet and Internet environments including Identity Directory, email, web, database, DNS and other server and application services.</p>
  </div>
  <div class="divider"></div>
  <div class="svc" style="left:218px;top:564px">
    <h3>Desktop Support</h3>
    <p>Brelvatix provides desktop computer support in Marrowdale including desktop and application installation, general troubleshooting, user support, backup implementation and anti-virus solutions.</p>
  </div>
  <div class="svc" style="left:493px;top:521px">
    <h3>Network Support</h3>
    <p>Servers and desktops operate in a networked environment and their deployment should always consider the network at large in order to provide the most effective performance and security. Our consultants draw upon existing network expertise to always consider the proper placement, configuration and functionality of computer systems within your network.</p>
  </div>
  <div class="svc" style="left:768px;top:524px">
    <h3>Security &amp; Backup<br>Solutions</h3>
    <p>The security of your computer systems should always be a primary concern in order to protect valuable resources and proper functionality. Our consultants are highly experienced in performing security assessments and implementing proper security and backup strategies for new and existing environments.</p>
  </div>
  <a class="btn view-all">View All</a>
</section>

<section class="blog">
  <h2>Excellence in Consulting, Every<br>Step of the Way</h2>
  <p class="intro">Lorem Ipsum is simply dummy text of the printing and typesetting industry. Lorem Ipsum has been the industry's standard dummy text ever since the 1500s</p>
  <article class="post" style="left:188px">
    <div class="thumb" role="img" aria-label="Photo of two colleagues reviewing a computer screen in an office" style="background:linear-gradient(135deg,#3d2a24,#7b8a96 60%,#c9d2d8)"></div>
    <div class="date">01. Januar 2024</div>
    <h3>Basic Orrin OS<br>Troubleshooting Guide</h3>
  </article>
  <article class="post" style="left:469px">
    <div class="thumb" role="img" aria-label="Photo of a technician repairing a laptop on a workbench" style="background:linear-gradient(160deg,#3a3f52,#5a4a3c 55%,#8a6a4c)"></div>
    <div class="date">01. Januar 2024</div>
    <h3>How to Repair a Damaged<br>Hard Drive Using DiskMend</h3>
  </article>
  <article class="post" style="left:751px">
    <div class="thumb" role="img" aria-label="Photo of hands typing on a laptop keyboard" style="background:linear-gradient(135deg,#2e3a44,#8c8f92 50%,#b5825e)"></div>
    <div class="date">01. Januar 2024</div>
    <h3>Perform a Clean Installation<br>of Orrin OS</h3>
  </article>
</section>

<footer class="footer">
  <div class="logo-text">brelvatix</div>
  <nav class="social">
    <a class="active">WorkLattice</a>
    <a>Chirpline</a>
    <a>Pallgrove</a>
    <a>Vidrelay</a>
  </nav>
  <nav class="foot-nav"><a>Home</a><a>About</a><a>Services</a><a>Resources</a><a>Contact</a></nav>
  <div class="foot-contact" style="top:110px">
    <span>555-014-2290</span>
    <svg width="15" height="15" viewBox="0 0 24 24"><path d="M6.6 10.8a15.1 15.1 0 006.6 6.6l2.2-2.2c.3-.3.7-.4 1-.2 1.1.4 2.3.6 3.6.6.6 0 1 .4 1 1V20c0 .6-.4 1-1 1A17 17 0 013 4c0-.6.4-1 1-1h3.5c.6 0 1 .4 1 1 0 1.3.2 2.5.6 3.6.1.3 0 .7-.2 1z" fill="#f0912c"/></svg>
  </div>
  <div class="foot-contact" style="top:139px">
    <span>info@brelvatix.com</span>
    <svg width="15" height="12" viewBox="0 0 15 12"><rect width="15" height="12" rx="1" fill="#f0912c"/><path d="M1 1.5l6.5 5 6.5-5" stroke="#262626" stroke-width="1.4" fill="none"/></svg>
  </div>
</footer>

<div class="copyright">Copyright © 2024 Brelvatix Consulting Inc</div>

</body>
</html>
```